Business Card Design

The attached file is what i need on the front of the card. No details to be changed.

On the back could i have as a heading:
We buy for cash $$$
Deceased estates house lots
Antiques, vintage furniture, bikes, kitchenware, automobile, toys,
sports memorabilia, books, records, signage,farm equipment and fashion.

Industry/Entity Type

House

```html
<!DOCTYPE html>
<html lang="en">
<head>
<meta charset="utf-8">
<title>Larkfield Vintage – Business Card</title>
<link rel="stylesheet" href="https://fonts.googleapis.com/css2?family=Arimo:ital,wght@0,400;0,700;1,700&family=Great+Vibes&family=Kaushan+Script&display=swap">
<style>
  :root{
    --page:#e9e4dc;
    --red-deep:#5e0a0d;
    --red:#8d1417;
    --red-light:#b3262a;
    --gold:#d8b526;
    --gold-soft:#e6cd5a;
    --paper:#f4f4f4;
    --ink:#2a2a2a;
    --accent:#d11a22;
    --social:#3b5998;
  }
  *{box-sizing:border-box;margin:0;padding:0}
  html,body{width:1200px;height:1023px;overflow:hidden}
  body{background:var(--page);font-family:"Arimo",Arial,sans-serif;color:var(--ink);position:relative}
  .card{position:absolute;left:240px;width:720px;height:411px;overflow:hidden;background:var(--paper);box-shadow:0 6px 18px rgba(0,0,0,.18)}
  .card--front{top:70px}
  .card--back{top:541px}
  .red-field{position:absolute;left:0;top:0;width:100%;background:radial-gradient(ellipse at 40% 45%,var(--red-light) 0%,var(--red) 45%,var(--red-deep) 100%)}
  .gold-rule{position:absolute;left:0;width:100%;height:5px;background:var(--gold)}

  /* front */
  .card--front .red-field{height:250px}
  .card--front .gold-rule{top:250px}
  .logo-frame{position:absolute;left:150px;top:22px;width:300px;height:150px;border-radius:6px;background:radial-gradient(ellipse at center,rgba(216,181,38,.28) 0%,rgba(216,181,38,.08) 70%,rgba(216,181,38,0) 100%)}
  .brand-name{position:absolute;left:150px;top:78px;width:300px;text-align:center;font-weight:700;font-size:34px;color:var(--gold-soft)}
  .tagline{position:absolute;left:0;top:185px;width:100%;text-align:center;font-family:"Great Vibes",cursive;font-size:38px;line-height:44px;color:#f1ece4;white-space:nowrap}
  .hours{position:absolute;left:40px;top:278px;font-size:15px;line-height:19px}
  .hours .open{color:var(--accent);font-weight:700;font-size:20px;margin-bottom:4px}
  .hours .slot{padding-left:40px}
  .contact{position:absolute;right:36px;top:278px;text-align:right;font-size:14px;line-height:24px}
  .contact .web{letter-spacing:1px;color:#444}
  .contact .web i{display:inline-block;width:12px;height:12px;background:var(--social);vertical-align:-1px;margin-left:6px}
  .contact .phone{font-weight:700;font-size:16px}
  .contact .phone svg{vertical-align:-2px;margin-right:6px}

  /* back */
  .card--back .red-field{height:208px}
  .card--back .gold-rule{top:208px}
  .buy-head{position:absolute;left:0;top:20px;width:100%;text-align:center;color:#fff;font-weight:700}
  .buy-head .h1{font-size:24px;line-height:30px}
  .buy-head .h2{font-size:19px;line-height:24px}
  .buy-head .browse{font-family:"Kaushan Script",cursive;font-weight:400;font-size:20px;line-height:28px}
  .buy-head .range{font-size:14px;line-height:18px;margin-top:4px}
  .stock{position:absolute;left:0;top:220px;width:100%;text-align:center;font-size:12.5px;line-height:14.2px}
  .stock b{color:var(--accent)}
  .stall{position:absolute;right:40px;bottom:10px;font-family:"Kaushan Script",cursive;font-size:15px;color:#111}
</style>
</head>
<body>
  <section class="card card--front" aria-label="Card front">
    <div class="red-field"></div>
    <div class="logo-frame" role="img" aria-label="Gold ornamental scroll frame around the shop name"></div>
    <div class="brand-name">Larkfield Vintage</div>
    <div class="tagline">Larkfield - Retro clothing &amp; Collectables</div>
    <div class="gold-rule"></div>
    <div class="hours">
      <div class="open">OPEN 6 DAYS A WEEK</div>
      <div class="slot">10:00am - 5:00pm</div>
      <div class="slot">CLOSED TUESDAYS</div>
      <div>88 Orchard Hill Rd. Merricks 3916</div>
      <div>Email: info@larkfieldvintage.com.au</div>
    </div>
    <div class="contact">
      <div class="web">www.larkfieldvintage.com.au<i></i></div>
      <div class="phone"><svg width="12" height="12" viewBox="0 0 12 12"><rect width="12" height="12" rx="2" fill="#d11a22"/><path d="M3.5 2.8c.4-.3.8-.2 1 .2l.6 1.2c.2.4 0 .7-.3.9l-.4.3c.4.9 1 1.5 1.9 1.9l.3-.4c.2-.3.5-.5.9-.3l1.2.6c.4.2.5.6.2 1l-.5.6c-2.6.3-5.4-2.5-5.1-5.1z" fill="#fff"/></svg>59 412 086</div>
      <div class="phone"><svg width="12" height="12" viewBox="0 0 12 12"><rect width="12" height="12" rx="2" fill="#d11a22"/><rect x="4" y="2" width="4" height="8" rx="1" fill="#fff"/></svg>0412 555 308</div>
    </div>
  </section>

  <section class="card card--back" aria-label="Card back">
    <div class="red-field"></div>
    <div class="buy-head">
      <div class="h1">We buy for cash $$$</div>
      <div class="h2">Deceased estates house lots</div>
      <div class="browse">Call in and browse!</div>
      <div class="range">Antiques, vintage furniture,<br>bikes, kitchenware, automobile,<br>toys,sports memorabilia,books, records,<br>signage,farm equipment and fashion.</div>
    </div>
    <div class="gold-rule"></div>
    <div class="stock">
      <div><b>Ceramics:</b> from all eras and from all over the world</div>
      <div><b>Furniture:</b> rustic, restored, chairs, teak, tables</div>
      <div><b>Clothes:</b> mens &amp; ladies, shirts, dresses, shoes, jewellery</div>
      <div><b>Glassware:</b> depression glass, uranium, retro, murano,</div>
      <div>Scandinavian, Czechoslovakian</div>
      <div><b>Bikes:</b> dragsters, skateboards &amp; bike parts</div>
      <div><b>Kitchenalia:</b> canisters, glasses, utensils items from all eras</div>
      <div>Books: from all eras</div>
      <div><b>Records:</b> a variety of eras 50s, 60s, 70s, 80s</div>
      <div><b>Toys:</b> model cars, pedal cars, dolls</div>
      <div>Coins &amp; Stamps, Military &amp; Watches and so much more</div>
    </div>
    <div class="stall">Stallholder enquiries welcome!</div>
  </section>
</body>
</html>
```